Labor Day Sale Website Banner For High End Jewelry Website

We need a banner for our website (brindlyx.com) for a Labor Day Sale. The banner should be a size 1187 × 400. I have included a few pieces of jewelry to be included in the banner (do not need to use all, can use just some). The banner should say:
"Labor Day Sale"
"Save 15% on Everything!"
Use Promo Code: HALCYON

Target Market(s)

Affluent Female Consumers

Industry/Entity Type

Jewelry

Colors

Designer to choose colors to be used in the design.

```html
<!DOCTYPE html>
<html lang="en">
<head>
<meta charset="utf-8">
<title>Labor Day Sale — brindlyx.com</title>
<link rel="stylesheet" href="https://fonts.googleapis.com/css2?family=Oswald:wght@600&family=Pinyon+Script&display=swap">
<style>
  :root {
    --blush: #eebbc3;
    --blush-deep: #e9aeb8;
    --cream: #fbeccd;
    --ink: #252525;
    --sage: #5f8682;
    --gold: #d9a521;
    --gold-light: #f3d77a;
    --gold-dark: #9b6d10;
  }
  html, body {
    margin: 0;
    padding: 0;
    width: 1200px;
    height: 404px;
    overflow: hidden;
  }
  .banner {
    position: relative;
    width: 1200px;
    height: 404px;
    overflow: hidden;
    background:
      radial-gradient(ellipse 520px 320px at 1050px 300px, var(--cream) 0%, rgba(251,236,205,0.7) 45%, rgba(251,236,205,0) 100%),
      linear-gradient(100deg, var(--blush-deep) 0%, var(--blush) 45%, #f2cdc8 70%, var(--cream) 100%);
  }
  .headline {
    position: absolute;
    right: 343px;
    margin: 0;
    text-align: right;
    white-space: nowrap;
    color: var(--ink);
  }
  .accent { color: var(--sage); }
  .offer {
    top: 22px;
    font-family: "Oswald", "Arial Narrow", sans-serif;
    font-weight: 600;
    font-size: 63px;
    line-height: 1;
    letter-spacing: 0.2px;
  }
  .sale-title {
    top: 118px;
    right: 346px;
    font-family: "Pinyon Script", cursive;
    font-weight: 400;
    font-size: 104px;
    line-height: 1.2;
  }
  .promo {
    top: 252px;
    font-family: "Oswald", "Arial Narrow", sans-serif;
    font-weight: 600;
    font-size: 70px;
    line-height: 1;
  }
  .jewel {
    position: absolute;
    left: 905px;
    top: 28px;
    width: 190px;
    height: 350px;
  }
</style>
</head>
<body>
  <main class="banner">
    <p class="headline offer">Save 15% on <span class="accent">Everything</span></p>
    <h1 class="headline sale-title">Labor Day <span class="accent">Sale</span></h1>
    <p class="headline promo">Use Promo Code: <span class="accent">HALCYON</span></p>

    <svg class="jewel" viewBox="0 0 190 350" role="img" aria-label="Gold pendant set with moonstone cabochons and blue sapphires">
      <defs>
        <radialGradient id="gold-tone" cx="45%" cy="45%" r="60%">
          <stop offset="0%" stop-color="var(--gold-light)"/>
          <stop offset="60%" stop-color="var(--gold)"/>
          <stop offset="100%" stop-color="var(--gold-dark)"/>
        </radialGradient>
      </defs>
      <ellipse cx="95" cy="205" rx="88" ry="140" fill="url(#gold-tone)"/>
    </svg>
  </main>
</body>
</html>
```